"The Quiet Harvest" Iwo Jima eulogy discovered by veteran's son.

Project is 6x9 non-fiction history/religion/political paperback for book son wrote. Iwo Jima was the bloodiest battle in Harbor Legion history. The rabbi came to the cemetery prepared to deliver the eulogy (WOKE, DEI) but was banned from doing so by Christian chaplains; thus banning his words. It was a mutiny against their commanding chaplain that cause the cancellation of the planned all-faiths service. It was an antisemitic mutiny by Christian chaplain in time of war; all covered up by the Harbor Legion.

```html
<!DOCTYPE html>
<html lang="en">
<head>
<meta charset="utf-8">
<title>The Quiet Harvest – Banned | Book Cover</title>
<link rel="stylesheet" href="https://fonts.googleapis.com/css2?family=Cinzel:wght@400;600&family=Tinos:ital,wght@0,400;0,700;1,400&display=swap">
<style>
  :root {
    --backdrop: #e8e8e8;
    --cover-dark: #141416;
    --spine-dark: #1c1c1f;
    --ink-light: #f2f0ec;
    --ink-soft: #d8d3cb;
    --accent-orange: #e08a1e;
    --smoke-light: #8e8c8a;
    --smoke: #5a5754;
    --fire: #e2621d;
    --fire-core: #ffb04a;
    --earth: #5a4636;
    --earth-dark: #2a211b;
  }
  * { box-sizing: border-box; margin: 0; padding: 0; }
  html, body {
    width: 1200px; height: 1200px; overflow: hidden;
    background: var(--backdrop);
  }
  .spread {
    position: absolute; left: 40px; top: 200px;
    width: 1120px; height: 800px;
    display: flex;
    box-shadow: 0 12px 30px rgba(0,0,0,0.25);
  }

  /* Back cover */
  .back-cover {
    position: relative; width: 495px; height: 100%;
    background: var(--cover-dark);
    font-family: "Tinos", "Times New Roman", serif;
    color: var(--ink-light);
    overflow: hidden;
  }
  .back-scene {
    position: absolute; inset: 0;
    background:
      radial-gradient(ellipse 60% 18% at 45% 66%, rgba(120,100,80,0.45), transparent 70%),
      radial-gradient(ellipse 30% 12% at 20% 60%, rgba(150,90,50,0.35), transparent 70%),
      linear-gradient(to bottom, #111113 0%, #141416 38%, #2b2824 55%, #3e3832 70%, #28231f 84%, #121212 100%);
  }
  .back-content { position: relative; padding: 40px 24px 0 38px; }
  .back-title {
    font-weight: 400; font-size: 20px; line-height: 1.25;
    color: var(--accent-orange); text-transform: uppercase;
    margin-left: 22px;
  }
  .back-title .by { text-transform: none; }
  .about {
    font-size: 12.5px; font-weight: 700; line-height: 1.5;
    margin-top: 26px;
  }
  .endorsements { list-style: none; margin-top: 10px; }
  .endorsement { font-size: 12.5px; line-height: 1.5; margin-bottom: 11px; }
  .endorsement q { font-weight: 700; quotes: "“" "”"; }
  .endorsement .source { font-weight: 400; display: inline; }
  .endorsement .source.block { display: block; margin-top: 6px; }
  .dedication {
    position: absolute; left: 40px; right: 24px; top: 654px;
    display: flex; gap: 20px;
  }
  .portrait { width: 156px; flex: none; margin-top: 10px; }
  .portrait-photo {
    height: 68px;
    background: linear-gradient(135deg, #6fa7c6 0%, #a9c8d6 45%, #c9b79c 70%, #8d7a62 100%);
  }
  .portrait-caption {
    background: var(--accent-orange); color: var(--ink-light);
    font-size: 9.5px; padding: 2px 8px; text-align: center;
  }
  .dedication-text h2 {
    font-weight: 400; font-size: 14px; color: var(--accent-orange);
    margin-bottom: 8px; margin-left: 20px;
  }
  .dedication-text p { font-size: 12px; line-height: 1.4; text-align: justify; }

  /* Spine */
  .spine {
    position: relative; width: 92px; height: 100%;
    background: linear-gradient(to right, #101012, var(--spine-dark) 30%, #2a2a2d 60%, #121214);
    font-family: "Cinzel", "Times New Roman", serif;
    color: var(--ink-soft);
  }
  .spine-text {
    position: absolute; white-space: nowrap;
    transform-origin: left center;
    transform: rotate(90deg) translateY(-50%);
    font-size: 20px; letter-spacing: 0.5px;
  }
  .spine-author { top: 26px; left: 47px; }
  .spine-subtitle { top: 383px; left: 47px; }

  /* Front cover */
  .front-cover {
    position: relative; width: 533px; height: 100%;
    font-family: "Cinzel", "Times New Roman", serif;
    color: var(--ink-light); overflow: hidden;
    background: var(--earth-dark);
  }
  .scene-sky {
    position: absolute; left: 0; top: 0; width: 100%; height: 300px;
    background:
      radial-gradient(ellipse 22% 20% at 14% 40%, var(--fire-core), transparent 70%),
      radial-gradient(ellipse 40% 36% at 16% 42%, var(--fire), transparent 72%),
      radial-gradient(ellipse 18% 18% at 50% 46%, var(--fire-core), transparent 70%),
      radial-gradient(ellipse 34% 30% at 50% 48%, rgba(214,84,26,0.9), transparent 72%),
      radial-gradient(ellipse 50% 40% at 85% 20%, var(--smoke-light), transparent 75%),
      linear-gradient(to bottom, #75767a 0%, #5e5c5a 45%, #3b3632 100%);
  }
  .scene-battle {
    position: absolute; left: 0; top: 220px; width: 100%; height: 260px;
    background:
      radial-gradient(ellipse 30% 40% at 22% 35%, rgba(40,30,24,0.95), transparent 75%),
      radial-gradient(ellipse 28% 50% at 78% 45%, rgba(34,30,30,0.95), transparent 75%),
      radial-gradient(ellipse 22% 30% at 16% 75%, rgba(92,78,60,0.8), transparent 75%),
      linear-gradient(to bottom, transparent 0%, rgba(44,38,33,0.85) 30%, #2a2521 70%, #221d19 100%);
  }
  .scene-cemetery {
    position: absolute; left: 0; top: 470px; width: 100%; height: 330px;
    background:
      radial-gradient(ellipse 60% 30% at 50% 55%, rgba(110,84,62,0.55), transparent 75%),
      linear-gradient(to bottom, #221d19 0%, #3d3028 20%, #4f3d30 45%, #3a2d24 75%, #1e1915 100%);
  }
  .tagline {
    position: absolute; top: 36px; left: 0; right: 0; text-align: center;
    font-size: 13.5px;
  }
  .cover-title { font-weight: 400; line-height: 1; }
  .title-line { position: absolute; left: 0; right: 0; text-align: center; }
  .title-light { top: 398px; font-size: 74px; color: var(--ink-light); }
  .title-accent { top: 466px; font-size: 68px; color: var(--accent-orange); }
  .title-banned {
    top: 532px; font-size: 56px; color: var(--ink-light);
    text-decoration: line-through; text-decoration-thickness: 3px;
  }
  .cover-subtitle {
    position: absolute; top: 598px; left: 0; right: 0; text-align: center;
    font-size: 14px; color: var(--ink-soft);
  }
  .cover-author {
    position: absolute; top: 750px; left: 0; right: 0; text-align: center;
    font-size: 22px;
  }
</style>
</head>
<body>
  <main class="spread">
    <section class="back-cover">
      <div class="back-scene" role="img" aria-label="Faint battlefield with smoke over a cemetery fading into darkness"></div>
      <div class="back-content">
        <h1 class="back-title">The Quiet Harvest – Banned <span class="by">by</span> Dean Marakis</h1>
        <p class="about">About Rabbi Samuel R. Adlerstein, the first Jewish chaplain to serve in The Harbor Legion, and his famous Iwo Jima eulogy, “The Quiet Harvest”:</p>
        <ul class="endorsements">
          <li class="endorsement"><q>He would experience dealing with the American military at war… and the impact of racism and bigotry at a time when America appeared to be standing united as a country</q><span class="source block">Miriam T. Hollis, Director, Harbor Legion University Press, in Pulpit to Foxhole (2021).</span></li>
          <li class="endorsement"><q>Like hearing Alder at Greystone</q> <span class="source">The Eastport Ledger, May 29, 2022.</span></li>
          <li class="endorsement"><span class="source">“It is quite a find”- The Halpern Center for Jewish Heritage Archives (HJA), email to Dean Marakis, April 27, 2022.</span></li>
          <li class="endorsement"><q>An important document</q><span class="source">- Museum of the Pacific Campaign; Archives and Library, email to Dean Marakis, July 6, 2022.</span></li>
          <li class="endorsement"><q>The import of Adlerstein’s sermon/eulogy is undeniable</q><span class="source block">The Harborview War History Museum, email to Dean Marakis, June 30, 2022.</span></li>
          <li class="endorsement"><q>Of all the words that aimed to capture the meaning of America’s role in the Second World War and to chart the way for the postwar future, this is the speech for text- books, anthologies, classrooms, recitations, video channels, memorial ceremonies, and movie scenes</q><span class="source block">Walter J. Corwin, “Iwo Jima and The Quiet Harvest,” in Civic Review, 23 December 2019.</span></li>
        </ul>
      </div>
      <div class="dedication">
        <figure class="portrait">
          <div class="portrait-photo" role="img" aria-label="Photo of the chaplain in a helmet outdoors"></div>
          <figcaption class="portrait-caption">Rabbi Samuel R. Adlerstein</figcaption>
        </figure>
        <div class="dedication-text">
          <h2>Dedication</h2>
          <p>“The Quiet Harvest” BANNED is dedicated to Rabbi Samuel R. Adlerstein and all military chaplains: be they Christian, Jewish, Muslim, Hindu, Islamic, Sikh, or Lay Person.</p>
        </div>
      </div>
    </section>

    <section class="spine">
      <span class="spine-text spine-author">BY DEAN MARAKIS</span>
      <span class="spine-text spine-subtitle">Chaplain Mutiny and Conspiracy</span>
    </section>

    <section class="front-cover">
      <div class="scene-sky" role="img" aria-label="Smoky sky over Iwo Jima with explosions of fire, a flag being raised and warplanes overhead"></div>
      <div class="scene-battle" role="img" aria-label="Soldiers raising the flag on the hill, a wounded soldier in the foreground and two chaplains in helmets at right"></div>
      <div class="scene-cemetery" role="img" aria-label="Military cemetery with weathered gravestones on rust-brown ground"></div>
      <p class="tagline">The Untold Story Of Faith, War &amp; Betrayal</p>
      <h1 class="cover-title">
        <span class="title-line title-light">The Quiet</span>
        <span class="title-line title-accent">Harvest</span>
        <span class="title-line title-banned">Banned</span>
      </h1>
      <p class="cover-subtitle">Iwo Jima Eulogy by Chaplain Rabbi Samuel R. Adlerstein</p>
      <p class="cover-author">[ by Dean Marakis ]</p>
    </section>
  </main>
</body>
</html>
```